Develop a Corporate Identity for Qulbo

We are a global sourcing firm. the company name is QULBO. Slogan is SOURCING THE WORLD. Has to be Unique. Has to have world standard.

```html
<!DOCTYPE html>
<html lang="en">
<head>
<meta charset="utf-8">
<title>Qulbo Business Card</title>
<link href="https://fonts.googleapis.com/css2?family=Open+Sans:ital,wght@0,700;1,600;1,700&display=swap" rel="stylesheet">
<style>
  :root {
    --backdrop-center: #f4f4f4;
    --backdrop-edge: #c9c9c9;
    --paper: #fbfbfb;
    --brand-blue: #1f5aa8;
    --brand-blue-light: #3f8fd8;
    --ink-light: #ffffff;
    --dark-center: #444444;
    --dark-edge: #171717;
    --faint-circle: #dfe6ee;
  }
  * { margin: 0; padding: 0; box-sizing: border-box; }
  html, body { width: 1200px; height: 801px; overflow: hidden; }
  body {
    position: relative;
    background: radial-gradient(ellipse at 50% 45%, var(--backdrop-center) 0%, var(--backdrop-edge) 100%);
    font-family: "Open Sans", Arial, sans-serif;
  }
  .card {
    position: absolute;
    width: 576px;
    height: 320px;
    border-radius: 17px;
    overflow: hidden;
    box-shadow: 0 2px 6px rgba(0,0,0,0.25);
  }
  .card-front { left: 313px; top: 60px; background: var(--paper); }
  .card-back {
    left: 311px; top: 419px; width: 578px;
    background: radial-gradient(ellipse at 50% 50%, var(--dark-center) 0%, var(--dark-edge) 80%);
  }

  .front-faint-circle {
    position: absolute; left: -4px; top: 172px;
    width: 136px; height: 136px; border-radius: 50%;
    background: var(--faint-circle); opacity: 0.7;
  }
  .front-accent-vertical {
    position: absolute; left: 282px; top: 0; width: 7px; height: 315px;
    background: var(--brand-blue);
  }
  .front-accent-bottom {
    position: absolute; left: 0; top: 306px; width: 289px; height: 9px;
    background: var(--brand-blue);
  }
  .brand-lockup { position: absolute; display: flex; align-items: center; }
  .brand-mark { border-radius: 50%; background: var(--brand-blue-light); flex: none; }
  .brand-name { font-weight: 700; color: var(--brand-blue-light); line-height: 1; letter-spacing: 1px; }
  .brand-slogan { font-weight: 700; color: var(--brand-blue-light); line-height: 1; letter-spacing: 0.6px; }

  .front-lockup { left: 25px; top: 62px; }
  .front-lockup .brand-mark { width: 74px; height: 74px; margin-right: 8px; }
  .front-lockup .brand-name { font-size: 44px; color: var(--brand-blue); }
  .front-lockup .brand-slogan { font-size: 12.5px; margin-top: 4px; color: var(--brand-blue); }

  .front-website {
    position: absolute; left: 128px; top: 279px;
    font-size: 14px; font-weight: 700; font-style: italic; color: var(--brand-blue);
  }

  .front-dark-panel {
    position: absolute; left: 296px; top: 0; right: 0; bottom: 0;
    background: radial-gradient(ellipse at 45% 55%, var(--dark-center) 0%, var(--dark-edge) 85%);
  }
  .contact-person {
    position: absolute; left: 146px; top: 28px;
    color: var(--ink-light); font-weight: 700; font-style: italic; font-size: 16px; line-height: 21px;
  }
  .contact-details {
    position: absolute; left: 33px; top: 170px; list-style: none;
    color: var(--ink-light); font-weight: 700; font-style: italic; font-size: 14.5px; line-height: 20.8px;
    white-space: nowrap;
  }

  .back-lockup { left: 131px; top: 108px; }
  .back-lockup .brand-mark { width: 102px; height: 102px; margin-right: 10px; }
  .back-lockup .brand-name { font-size: 56px; }
  .back-lockup .brand-slogan { font-size: 16.5px; margin-top: 6px; }
</style>
</head>
<body>
  <section class="card card-front">
    <div class="front-faint-circle"></div>
    <div class="brand-lockup front-lockup">
      <div class="brand-mark"></div>
      <div class="brand-text">
        <div class="brand-name">QULBO</div>
        <div class="brand-slogan">SOURCING THE WORLD</div>
      </div>
    </div>
    <div class="front-website">www.qulbo-trade.com</div>
    <div class="front-accent-vertical"></div>
    <div class="front-accent-bottom"></div>

    <div class="front-dark-panel">
      <div class="contact-person">
        <div class="contact-name">Name</div>
        <div class="contact-title">Designation</div>
      </div>
      <ul class="contact-details">
        <li>Address : 48 Harbor Lane</li>
        <li>Postal Code : 7319</li>
        <li>Cell # : 014 782 3506</li>
        <li>Fax # : 014 782 3507</li>
        <li>Email : hello@qulbo-trade.com</li>
        <li>www.qulbo-trade.com</li>
      </ul>
    </div>
  </section>

  <section class="card card-back">
    <div class="brand-lockup back-lockup">
      <div class="brand-mark"></div>
      <div class="brand-text">
        <div class="brand-name">QULBO</div>
        <div class="brand-slogan">SOURCING THE WORLD</div>
      </div>
    </div>
  </section>
</body>
</html>
```